Electrical Contractor Brochure, Folder and Letter Head

Barrowfield Electrical Ltd. is an Edmonton based electrical contractor focusing on commercial and industrial electrical services. Our target market is manufacturing facilities, warehouses and commercial buildings.

We want to seem larger than we are with service vehicles and electricians ready to dispatch to service calls and new installations. Our key color is the blue in the logo. The BFE logo is well branded in Edmonton and should be on the brochure.

We are looking for a tri-fold brochure, full-page brochure with folder sleeves and a letter head.
Updates

Please ignore the second page of copy.  I only want the electrical content in the brochure.  This is my mistake.  Please use only the first page of copy.

Industry/Entity Type

Electrical

Requirements
Must have
• Many background pics of the services, electricians and projects. I like the faded BFE logo in the background of the letterhead! Folder Size A4
Nice to have
• Try the pic named Cover Pic1 to on the front of the brochure.
Should not have
• DO NOT USE ANY WEBSITE CONTENT. THIS IS NOT OUR BUSINESS. PLEASE USE ONLY CONTENT AND COLOR FROM THE ATTACHED FILES!!

```html
<!DOCTYPE html>
<html lang="en">
<head>
<meta charset="utf-8">
<title>Barrowfield Electrical Ltd. – Letterhead</title>
<link rel="stylesheet" href="https://fonts.googleapis.com/css2?family=Open+Sans:wght@400;700&display=swap">
<style>
  :root {
    --brand-blue: #1f5fae;
    --brand-navy: #1b2f6e;
    --ink: #3a3a3a;
    --rule: #b9b9b9;
    --band-grey: #7a7a7a;
    --watermark: #e9e9f1;
    --paper: #ffffff;
  }
  html, body {
    margin: 0;
    padding: 0;
    overflow: hidden;
    background: var(--paper);
  }
  .letterhead {
    position: relative;
    width: 1011px;
    height: 1200px;
    background: var(--paper);
    overflow: hidden;
    font-family: "Open Sans", Arial, sans-serif;
    color: var(--ink);
  }
  .brand {
    position: absolute;
    left: 56px;
    top: 92px;
    display: flex;
    align-items: center;
    gap: 12px;
  }
  .brand-square {
    width: 22px;
    height: 22px;
    background: var(--brand-blue);
  }
  .brand-name {
    font-size: 27px;
    font-weight: 700;
    color: var(--brand-navy);
    letter-spacing: 0.2px;
    white-space: nowrap;
  }
  .contact {
    position: absolute;
    left: 784px;
    top: 70px;
    height: 100px;
    border-left: 1px solid var(--rule);
    padding-left: 15px;
    font-size: 14.5px;
    line-height: 18px;
  }
  .contact-address { margin: 0 0 12px; }
  .contact-line {
    display: flex;
    align-items: center;
    gap: 5px;
    margin: 0 0 2px;
  }
  .contact-line svg { width: 11px; height: 11px; fill: var(--brand-blue); }
  .watermark {
    position: absolute;
    left: 145px;
    top: 575px;
    width: 723px;
    text-align: center;
    font-size: 270px;
    font-weight: 700;
    line-height: 1;
    letter-spacing: 6px;
    color: var(--watermark);
    user-select: none;
  }
  .footer-bands {
    position: absolute;
    left: 0;
    bottom: 0;
    width: 1011px;
    height: 40px;
  }
  .footer-url {
    position: absolute;
    right: 96px;
    bottom: 11px;
    font-size: 15px;
    letter-spacing: 3.5px;
    color: #ffffff;
  }
</style>
</head>
<body>
<main class="letterhead">
  <header>
    <div class="brand">
      <span class="brand-square"></span>
      <span class="brand-name">Barrowfield Electrical Ltd.</span>
    </div>
    <address class="contact" style="font-style:normal">
      <p class="contact-address">00, complex name<br>City, state</p>
      <p class="contact-line">
        <svg viewBox="0 0 12 12" aria-hidden="true"><path d="M3 1l2 2.5-1.2 1.2a6 6 0 0 0 3.5 3.5L8.5 7 11 9l-1.5 2C5 11 1 7 1 2.5z"/></svg>
        123-456-0789
      </p>
      <p class="contact-line">
        <svg viewBox="0 0 12 12" aria-hidden="true"><rect x="3" y="1" width="6" height="4"/><rect x="1" y="5" width="10" height="5" rx="1"/></svg>
        123-456-0789
      </p>
      <p class="contact-line">
        <svg viewBox="0 0 12 12" aria-hidden="true"><path d="M1 4l5-3 5 3v6H1z"/><path d="M2 5l4 3 4-3" fill="none" stroke="#fff" stroke-width="1"/></svg>
        info@barrowfieldmail.com
      </p>
    </address>
  </header>

  <div class="watermark" aria-hidden="true">BFE</div>

  <footer>
    <svg class="footer-bands" viewBox="0 0 1011 40" aria-hidden="true">
      <polygon points="0,20 618,20 596,40 0,40" fill="var(--band-grey)"/>
      <polygon points="655,0 1011,0 1011,40 612,40" fill="var(--brand-blue)"/>
    </svg>
    <span class="footer-url">www.bfe-electrical.com</span>
  </footer>
</main>
</body>
</html>
```